Dozing Heron

Need a business card for our restaurant. Restaurant and Bar in the mountains of North Idaho. Rustic looking card

Contact Information for Business Card

rustic design, wood and metal looking, primarily neutral colors

Requirements
Must have
• Name, address, phone number, website, email address

```html
<!DOCTYPE html>
<html lang="en">
<head>
<meta charset="utf-8">
<title>Dozing Heron – Business Card</title>
<link rel="stylesheet" href="https://fonts.googleapis.com/css2?family=Jost:wght@500&family=Arimo:wght@400&display=swap">
<style>
  :root {
    --stage: #353535;
    --card: #2b2b2b;
    --ink: #f4f4f4;
    --rule: #9a9a9a;
    --emboss: #4a4a4a;
    --emboss-ink: #5a5a5a;
  }
  * { margin: 0; padding: 0; box-sizing: border-box; }
  html, body { width: 1200px; height: 1200px; overflow: hidden; background: var(--stage); }
  .canvas { position: relative; width: 1200px; height: 1200px; }

  .card {
    position: absolute;
    width: 688px;
    height: 393px;
    background: var(--card);
    border-radius: 14px;
  }
  .card--front { left: 267px; top: 158px; }
  .card--back { left: 262px; top: 653px; }

  .brand-seal {
    position: absolute;
    border-radius: 50%;
    display: flex;
    align-items: center;
    justify-content: center;
    text-align: center;
    font-family: "Jost", sans-serif;
    font-weight: 500;
    letter-spacing: 0.08em;
    text-transform: uppercase;
  }
  .card--front .brand-seal {
    left: 93px; top: 85px;
    width: 214px; height: 214px;
    border: 5px solid var(--ink);
    color: var(--ink);
    font-size: 24px;
    line-height: 1.15;
  }
  .card--back .brand-seal {
    left: 203px; top: 56px;
    width: 280px; height: 280px;
    border: 4px solid var(--emboss);
    color: var(--emboss-ink);
    font-size: 30px;
    line-height: 1.15;
  }

  .divider {
    position: absolute;
    left: 345px; top: 81px;
    width: 2px; height: 236px;
    background: linear-gradient(to bottom, transparent, var(--rule) 15%, var(--rule) 85%, transparent);
  }

  .contact {
    position: absolute;
    left: 370px; top: 92px;
    color: var(--ink);
    font-family: "Arimo", sans-serif;
  }
  .contact__name {
    font-family: "Jost", sans-serif;
    font-weight: 500;
    font-size: 28px;
    letter-spacing: 0.02em;
    line-height: 1;
  }
  .contact__role { font-size: 15px; margin-top: 6px; }
  .contact__address { font-size: 16px; line-height: 21px; margin-top: 20px; }
  .contact__list { list-style: none; margin-top: 12px; }
  .contact__list li {
    display: flex; align-items: center;
    font-size: 16px; line-height: 20.5px;
  }
  .contact__list svg { width: 14px; height: 14px; margin-right: 11px; fill: var(--ink); flex: none; }
</style>
</head>
<body>
<main class="canvas">
  <section class="card card--front">
    <div class="brand-seal">Dozing<br>Heron</div>
    <div class="divider"></div>
    <div class="contact">
      <h1 class="contact__name">MARA ELLISON</h1>
      <p class="contact__role">President</p>
      <p class="contact__address">218 Tamarack Way<br>Silver Hollow, Idaho 83999</p>
      <ul class="contact__list">
        <li><svg viewBox="0 0 16 16" aria-hidden="true"><path d="M3.5 1l2.5 3-1.5 2c.8 2 2.5 3.7 4.5 4.5l2-1.5 3 2.5-1.5 3C7 14 2 9 .5 2.5z"/></svg>555-210-4817</li>
        <li><svg viewBox="0 0 16 16" aria-hidden="true"><path d="M4 0h8a1 1 0 0 1 1 1v14a1 1 0 0 1-1 1H4a1 1 0 0 1-1-1V1a1 1 0 0 1 1-1zm.5 2v10h7V2zM8 13a1 1 0 1 0 0 2 1 1 0 0 0 0-2z"/></svg>555-390-6142</li>
        <li><svg viewBox="0 0 16 16" aria-hidden="true"><path d="M0 3h16v10H0zm1.5 1.5v.3L8 9l6.5-4.2v-.3zm0 2v5h13v-5L8 10.8z"/></svg>info@dozingheron.com</li>
        <li><svg viewBox="0 0 16 16" aria-hidden="true"><path d="M8 0a8 8 0 1 0 0 16A8 8 0 0 0 8 0zm-1 3c1 1 2 1 2 2s-2 1-2 2 2 1 2 3-2 2-3 3C4 12 2 10 2 8c0-2 2-4 5-5zm4 6c1 0 2 1 2 2l-2 2c-1 0-1-1-1-2s0-2 1-2z"/></svg>www.dozingheron.com</li>
      </ul>
    </div>
  </section>

  <section class="card card--back">
    <div class="brand-seal">Dozing<br>Heron</div>
  </section>
</main>
</body>
</html>
```